KFR T Coaching Website

We need a website to post videos, blogs and other information or links.
We teach Jujitsu , combatives, Metaphysical Coaching. I want to tach online and in person. Silver Harbor Institute Deals in several areas of Personal Protection and Coaching.
Training (Martial Arts / combative)
Emotional Intelligence
Leadership Development
Motivation
Our Log is attached.
Similar Websites to what we do ( we want to stand out better).
https://renwoskel.com/
https://bavomure.com/
https://crestlinevigorcoaching.com/
Training , Martial Arts, coaching
2 page

```html
<!DOCTYPE html>
<html lang="en">
<head>
<meta charset="utf-8">
<title>Silver Harbor Institute — KFR T Coaching</title>
<link href="https://fonts.googleapis.com/css2?family=Montserrat:wght@600;700;800&family=Roboto:wght@400;500;700&display=swap" rel="stylesheet">
<style>
:root{
  --red:#f04438;
  --black:#000;
  --panel:#141414;
  --white:#fff;
  --muted:#d6d6d6;
  --disc:#262626;
}
*{margin:0;padding:0;box-sizing:border-box}
html,body{width:1200px;height:4069px;overflow:hidden;background:var(--black)}
body{position:relative;font-family:'Roboto',sans-serif;color:var(--white)}
.abs{position:absolute}
.heading{font-family:'Montserrat',sans-serif;font-weight:800;text-transform:uppercase;letter-spacing:.5px}
.section-title{position:absolute;left:0;width:1200px;text-align:center;font-size:30px}
.section-title span{display:inline-flex;align-items:center;gap:14px}
.section-title span::before,.section-title span::after{content:"";width:44px;height:3px;background:var(--red)}
.lead{position:absolute;left:0;width:1200px;text-align:center;font-size:14.5px;line-height:25px;color:var(--muted)}
.btn{position:absolute;background:var(--red);color:var(--white);font-weight:700;font-size:14px;text-transform:uppercase;display:flex;align-items:center;justify-content:center;gap:10px;border-radius:2px}
.btn svg{flex:none}
.photo{position:absolute}
.ico{fill:none;stroke:var(--red);stroke-width:2.4;stroke-linecap:round;stroke-linejoin:round}

/* header */
.site-header{position:absolute;left:0;top:0;width:1200px;height:85px;background:var(--black);z-index:3}
.brand{position:absolute;left:126px;top:-40px;width:160px;height:165px;border-radius:0 0 80px 80px;background:var(--black);z-index:4;display:flex;flex-direction:column;align-items:center;justify-content:flex-end;padding-bottom:28px}
.brand-mark{width:44px;height:44px;border:2px solid var(--white);border-radius:50%;margin-bottom:8px}
.brand-name{font-family:'Montserrat',sans-serif;font-weight:700;font-size:11px;text-align:center;line-height:13px;color:var(--white)}
.nav{position:absolute;left:328px;top:33px;display:flex;gap:30px;font-size:14.5px;font-weight:500}
.nav .active{color:var(--red)}
.search{position:absolute;left:892px;top:24px;width:36px;height:36px;border-radius:50%;background:#2b2b2b;display:flex;align-items:center;justify-content:center}

/* hero */
.hero-photo{left:0;top:85px;width:1200px;height:725px;background:linear-gradient(90deg,#2a2825 0%,#5a5048 35%,#b9a89a 55%,#3f3a35 80%,#23211f 100%)}
.hero-shade{position:absolute;left:0;top:85px;width:700px;height:725px;background:linear-gradient(90deg,rgba(0,0,0,.55),rgba(0,0,0,0))}
.hero-kicker{left:73px;top:250px;font-size:28px;font-weight:700}
.hero-title{left:73px;top:302px;font-size:43px;line-height:47px}
.hero-text{left:73px;top:413px;width:420px;font-size:15px;line-height:26px}

/* services */
.service-card{position:absolute;top:970px;width:300px;height:220px;border:1px solid #5c1a16;padding:6px;background:#000}
.service-card div{width:100%;height:100%}
.service-label{position:absolute;top:1210px;width:300px;text-align:center;font-weight:700;font-size:18px}

/* about */
.about-bg{left:0;top:1250px;width:1200px;height:1700px;background:linear-gradient(180deg,#000 0%,#141414 12%,#0e0e0e 50%,#111 80%,#000 100%)}
.about-title{left:112px;top:1395px;font-size:30px;display:flex;align-items:center;gap:14px}
.about-title::after{content:"";width:42px;height:3px;background:var(--red)}
.about-text{left:112px;top:1440px;width:455px;font-size:15px;line-height:25.6px;text-align:justify;color:var(--muted)}
.about-circle{left:640px;top:1365px;width:452px;height:452px;border-radius:50%;border:2px solid var(--red);background:linear-gradient(135deg,#4a4f58,#7b8390 50%,#2c2f35)}

/* coaching */
.coach{position:absolute;top:2012px;width:240px;text-align:center}
.pin{width:146px;height:146px;margin:0 auto;border-radius:50%;border:2px solid #333;background:#121212;position:relative;display:flex;align-items:center;justify-content:center}
.pin::after{content:"";position:absolute;bottom:-14px;left:59px;border-top:16px solid #333;border-left:14px solid transparent;border-right:14px solid transparent}
.pin-inner{width:92px;height:92px;border-radius:50%;background:#1b1b1b;display:flex;align-items:center;justify-content:center}
.dot{width:18px;height:18px;border-radius:50%;border:2px solid #555;margin:25px auto 0;position:relative}
.dot::after{content:"";position:absolute;left:3px;top:3px;width:8px;height:8px;border-radius:50%;background:var(--red)}
.coach h3{font-family:'Montserrat',sans-serif;font-weight:700;font-size:16px;line-height:22px;margin-top:16px}
.coach p{font-size:14px;line-height:24px;color:var(--muted);margin-top:10px;padding:0 14px}

/* videos */
.video{position:absolute;top:2591px;width:312px;height:227px}
.video .play{position:absolute;left:141px;top:99px}

/* blogs */
.blog-card{position:absolute;border:1px solid #2e2e2e;border-radius:4px;background:#090909}
.date{position:absolute;width:76px;height:60px;background:var(--red);text-align:center;font-weight:700;line-height:22px;padding-top:7px}
.date b{display:block;font-size:26px;font-weight:500}
.date span{font-size:15px}
.blog-head{font-family:'Montserrat',sans-serif;font-weight:700;font-size:13px}
.blog-text{font-size:14px;line-height:22px;color:var(--muted)}
.read{color:var(--red);font-size:14px;display:flex;align-items:center;gap:8px}
.meta{display:flex;justify-content:center;align-items:center;gap:8px;font-size:13px;color:var(--red);font-weight:500}

/* footer */
.foot-logo{left:115px;top:3805px;width:195px;text-align:center}
.foot-logo .brand-mark{width:80px;height:80px;margin:0 auto 14px;border-width:3px;display:block}
.foot-logo p{font-family:'Montserrat',sans-serif;font-weight:700;font-size:17px;line-height:20px}
.foot-title{font-family:'Montserrat',sans-serif;font-weight:700;font-size:14px}
.foot-title::after{content:"";display:block;width:44px;height:2px;background:var(--red);margin-top:10px}
.foot-links{font-size:14px;line-height:30px}
.contact-row{display:flex;gap:14px;align-items:flex-start;font-size:14px;line-height:20px;margin-bottom:18px}
.contact-row i{flex:none;width:26px;height:26px;border-radius:50%;background:var(--disc);display:flex;align-items:center;justify-content:center}
.subscribe{left:834px;top:3865px;width:254px;height:36px;background:#1e1e1e;border-radius:18px;font-size:10px;color:#888;padding:12px 16px}
.subscribe-btn{left:1040px;top:3865px;width:48px;height:36px;background:var(--red);border-radius:0 18px 18px 0;display:flex;align-items:center;justify-content:center}
.social{position:absolute;top:3918px;width:30px;height:30px;border-radius:50%;background:var(--disc);display:flex;align-items:center;justify-content:center}
.social.on{background:var(--red)}
.social svg{fill:none;stroke:#fff;stroke-width:1.8;stroke-linecap:round;stroke-linejoin:round}
.chat{left:1124px;top:3940px;width:38px;height:38px;border-radius:50%;background:var(--red);display:flex;align-items:center;justify-content:center}
.bottom-bar{left:0;top:4009px;width:1200px;height:60px;background:#121212;font-size:13px;line-height:60px}
</style>
</head>
<body>

<header class="site-header">
  <div class="brand"><span class="brand-mark"></span><p class="brand-name">SILVER HARBOR<br>INSTITUTE</p></div>
  <nav class="nav"><span class="active">HOME</span><span>ABOUT US</span><span>SERVICES</span><span>VIDEOS</span><span>BLOG</span><span>CONTACT US</span></nav>
  <span class="search"><svg width="14" height="14" viewBox="0 0 14 14"><circle cx="6" cy="6" r="4.5" fill="none" stroke="#fff" stroke-width="2"/><path d="M9.5 9.5 13 13" stroke="#fff" stroke-width="2" stroke-linecap="round"/></svg></span>
  <span class="btn" style="left:966px;top:18px;width:122px;height:46px">Login <svg width="12" height="13" viewBox="0 0 12 13"><circle cx="6" cy="3.5" r="3" fill="#fff"/><path d="M0.5 13c0-3.5 2.5-5.5 5.5-5.5s5.5 2 5.5 5.5z" fill="#fff"/></svg></span>
</header>

<div class="photo hero-photo" role="img" aria-label="Smiling woman in conversation with a man across a table"></div>
<div class="hero-shade"></div>
<p class="abs heading hero-kicker" style="font-weight:700">Welcome to</p>
<h1 class="abs heading hero-title">Silver Harbor<br>Institute</h1>
<p class="abs hero-text">Lorem ipsum dolor sit ameted consectetur adipiscing elsed eiusmod tempor incididunt labore dolored magnat aliquad.</p>
<span class="btn" style="left:73px;top:485px;width:159px;height:47px">Get Started <svg width="14" height="14" viewBox="0 0 14 14"><circle cx="7" cy="7" r="7" fill="#fff"/><path d="M5.5 4 9 7l-3.5 3" fill="none" stroke="#f04438" stroke-width="2"/></svg></span>

<svg class="abs" style="left:0;top:660px" width="1200" height="160" viewBox="0 0 1200 160">
  <path d="M0 150 C250 60 450 20 650 25 C850 30 1050 80 1200 145 L1200 160 L0 160 Z" fill="#000"/>
  <path d="M0 100 L0 150 C60 150 150 148 235 150 C140 135 70 125 70 115 C300 40 520 15 720 25 C900 35 1080 90 1200 145 L1200 125 C1060 60 880 20 700 15 C480 10 250 50 0 100 Z" fill="var(--red)"/>
</svg>

<h2 class="heading section-title" style="top:822px"><span>Our Services</span></h2>
<p class="lead" style="top:880px">Lorem ipsum dolor sit amet, consectetur adipiscing elit, sed do eiusmod tempor incididunt labore dolore magna aliqua.<br>Ut enim ad minim veniam, quis nostrud exercitation ullamco laboris nisi ut aliquip ex ea commodo consequat.</p>

<div class="service-card" style="left:108px"><div role="img" aria-label="Two martial artists grappling on a training mat" style="background:linear-gradient(160deg,#7a5a3c,#c9c2b8 50%,#4a6fa8)"></div></div>
<div class="service-card" style="left:447px"><div role="img" aria-label="Man in a blue shirt in a fighting stance at a desk" style="background:linear-gradient(160deg,#6b5a45,#8a7560 45%,#3b4e6e)"></div></div>
<div class="service-card" style="left:787px"><div role="img" aria-label="Woman meditating on grass in a park" style="background:linear-gradient(180deg,#6d8a3a,#8fa64e 40%,#5e7a2c)"></div></div>
<p class="service-label" style="left:108px">JUJITSU</p>
<p class="service-label" style="left:447px">COMBATIVE</p>
<p class="service-label" style="left:787px">METAPHYSICAL COACHING</p>

<div class="photo about-bg" role="img" aria-label="Faint dark backdrop of an office meeting"></div>
<h2 class="abs heading about-title">About Us</h2>
<p class="abs about-text">Lorem ipsum dolor sit amet, consectetur adipiscing elit, sed do eiusmod tempor incididunt ut labore et dolore magna aliqua. Ut enim ad minim veniam, quis nostrud exercitation ullamco laboris nisi ut aliquip ex ea commodo consequat. Duis aute irure dolor in reprehenderit in voluptate velit esse cillum dolore eu fugiat nulla pariatur. Excepteur sint occaecat cupidatat non proident, sunt in culpa qui officia deserunt mollit anim id est laborumLorem ipsum dolor sit amet, consectetur adipiscing elit, sed do eiusmod tempor incididunt ut labore et dolore magna aliqua. Ut enim ad minim veniam, quis nostrud exercitation ullamco laboris nisi ut aliquip ex ea commodo consequat. Duis aute irure dolor in reprehenderit in voluptate velit esse cillum dolore eu fugia sint occaecat.</p>
<span class="btn" style="left:112px;top:1765px;width:158px;height:45px">Learn More <svg width="14" height="14" viewBox="0 0 14 14"><circle cx="7" cy="7" r="7" fill="#fff"/><path d="M5.5 4 9 7l-3.5 3" fill="none" stroke="#f04438" stroke-width="2"/></svg></span>
<div class="abs about-circle" role="img" aria-label="Woman and man working together at a laptop"></div>

<h2 class="heading section-title" style="top:1925px"><span>Our Coaching</span></h2>
<div class="coach" style="left:82px"><div class="pin"><div class="pin-inner">
  <svg class="ico" width="60" height="60" viewBox="0 0 60 60" aria-label="Training icon" role="img"><rect x="6" y="20" width="7" height="20" rx="2"/><rect x="13" y="16" width="7" height="28" rx="2"/><rect x="40" y="16" width="7" height="28" rx="2"/><rect x="47" y="20" width="7" height="20" rx="2"/><path d="M20 30h20"/></svg>
</div></div><div class="dot"></div><h3>TRAINING</h3><p>Lorem ipsum dolord consectetur adipiscing temporived incididunt labore dolore magna aliqua.</p></div>
<div class="coach" style="left:347px"><div class="pin"><div class="pin-inner">
  <svg class="ico" width="60" height="60" viewBox="0 0 60 60" aria-label="Emotional intelligence icon" role="img"><path d="M30 50 10 30a10 10 0 0 1 20-12 10 10 0 0 1 20 12z"/><path d="M14 31h9l3-6 5 12 3-6h12"/></svg>
</div></div><div class="dot"></div><h3>EMOTIONAL<br>INTELLIGENCE</h3><p>Lorem ipsum dolord consectetur labore dolore magna aliqua.</p></div>
<div class="coach" style="left:611px"><div class="pin"><div class="pin-inner">
  <svg class="ico" width="60" height="60" viewBox="0 0 60 60" aria-label="Leadership development icon" role="img"><path d="M16 52V8"/><path d="M16 10h28l-6 8 6 8H16"/><path d="M8 52h18"/></svg>
</div></div><div class="dot"></div><h3>LEADERSHIP<br>DEVELOPMENT</h3><p>Lorem ipsum dolord consectetur labore dolore magna aliqua.</p></div>
<div class="coach" style="left:876px"><div class="pin"><div class="pin-inner">
  <svg class="ico" width="60" height="60" viewBox="0 0 60 60" aria-label="Motivation icon" role="img"><rect x="8" y="36" width="14" height="16"/><rect x="22" y="28" width="14" height="24"/><rect x="36" y="40" width="14" height="12"/><path d="M29 8l3 6 6 1-4.5 4 1 6-5.5-3-5.5 3 1-6-4.5-4 6-1z"/></svg>
</div></div><div class="dot"></div><h3>MOTIVATION</h3><p>Lorem ipsum dolord consectetur adipiscing temporived incididunt labore dolore magna aliqua.</p></div>

<h2 class="heading section-title" style="top:2434px"><span>Our Videos</span></h2>
<p class="lead" style="top:2497px">Lorem ipsum dolor sit amet, consectetur adipiscing elit, sed do eiusmod tempor incididunt ut labore et dolore<br>magnad aliqua. Uted enim aded minim veniam, quis nostrud exercitation ullamcot laboris nisied.</p>
<div class="video" style="left:110px;background:linear-gradient(160deg,#e8e3dc,#c9a36a 60%,#b08a55)" role="img" aria-label="Video of children practising martial arts"><svg class="play" width="30" height="30" viewBox="0 0 30 30"><circle cx="15" cy="15" r="15" fill="#fff"/><path d="M12 9l9 6-9 6z" fill="#111"/></svg></div>
<div class="video" style="left:445px;background:linear-gradient(160deg,#efe2e0,#d7b7b0 55%,#c8c2bd)" role="img" aria-label="Video of a relaxation coaching session"><svg class="play" width="30" height="30" viewBox="0 0 30 30"><circle cx="15" cy="15" r="15" fill="#fff"/><path d="M12 9l9 6-9 6z" fill="#111"/></svg></div>
<div class="video" style="left:780px;background:linear-gradient(160deg,#2d3d52,#3f5f8e 55%,#8a7a4a)" role="img" aria-label="Video of a judo throw"><svg class="play" width="30" height="30" viewBox="0 0 30 30"><circle cx="15" cy="15" r="15" fill="#fff"/><path d="M12 9l9 6-9 6z" fill="#111"/></svg></div>

<h2 class="heading section-title" style="top:2957px"><span>Our Blogs</span></h2>
<div class="blog-card" style="left:113px;top:3030px;width:445px;height:455px">
  <div class="abs" style="left:7px;top:8px;width:430px;height:290px;background:linear-gradient(135deg,#6a8aa0,#4a5c70 50%,#b9c3c8)" role="img" aria-label="Man smiling at a laptop"></div>
  <div class="date" style="left:7px;top:8px"><b>10</b><span>Sep</span></div>
  <p class="abs blog-head" style="left:0;width:445px;text-align:center;top:330px;font-size:14px">LOREM IPSUM DOLOR SIT AMET</p>
  <p class="abs blog-text" style="left:25px;width:395px;text-align:center;top:357px">Lorem ipsum dolor sit amet, consectetur adipiscing elit, sed do eiusmod tempor incididunt ut labore et dolore magna</p>
  <div class="abs meta" style="left:0;width:445px;top:412px">
    <svg width="12" height="12" viewBox="0 0 12 12"><rect x="1" y="2" width="10" height="9" fill="none" stroke="#f04438" stroke-width="1.5"/><path d="M1 5h10M4 0.5v3M8 0.5v3" stroke="#f04438" stroke-width="1.5"/></svg>
    <span>Septembert 10,2022 &nbsp;| </span>
    <svg width="11" height="12" viewBox="0 0 11 12"><circle cx="5.5" cy="3.5" r="2.6" fill="none" stroke="#f04438" stroke-width="1.4"/><path d="M1 11.5c0-3 2-4.5 4.5-4.5s4.5 1.5 4.5 4.5" fill="none" stroke="#f04438" stroke-width="1.4"/></svg>
    <span>John Doe</span>
  </div>
</div>
<div class="blog-card" style="left:582px;top:3030px;width:502px;height:220px">
  <div class="abs" style="left:7px;top:10px;width:186px;height:198px;background:linear-gradient(135deg,#8a6d4a,#4b5a6b 60%,#d8d8d8)" role="img" aria-label="Man working at a computer in an office"></div>
  <div class="date" style="left:7px;top:10px"><b>10</b><span>Sep</span></div>
  <p class="abs blog-head" style="left:213px;top:30px">LOREM IPSUM DOLOR ONSECTETUR</p>
  <p class="abs blog-text" style="left:213px;top:55px;width:275px;font-size:13.5px">Lorem ipsum dolor sit amet, consectetur adipiscing elited sed do eiusmod tempor incididunt labored dolored magnad Uted. enim aded minim veniam quised.</p>
  <p class="abs read" style="left:213px;top:166px">Read More <svg width="13" height="13" viewBox="0 0 14 14"><circle cx="7" cy="7" r="7" fill="#f04438"/><path d="M5.5 4 9 7l-3.5 3" fill="none" stroke="#000" stroke-width="2"/></svg></p>
</div>
<div class="blog-card" style="left:582px;top:3263px;width:502px;height:220px">
  <div class="abs" style="left:7px;top:10px;width:186px;height:198px;background:linear-gradient(135deg,#e0dcd6,#6b5a48 55%,#2e2a26)" role="img" aria-label="Man at a desk with a desktop computer"></div>
  <div class="date" style="left:7px;top:10px"><b>10</b><span>Sep</span></div>
  <p class="abs blog-head" style="left:213px;top:30px">LOREM IPSUM DOLOR ONSECTETUR</p>
  <p class="abs blog-text" style="left:213px;top:55px;width:275px;font-size:13.5px">Lorem ipsum dolor sit amet, consectetur adipiscing elited sed do eiusmod tempor incididunt labored dolored magnad Uted. enim aded minim veniam quised.</p>
  <p class="abs read" style="left:213px;top:166px">Read More <svg width="13" height="13" viewBox="0 0 14 14"><circle cx="7" cy="7" r="7" fill="#f04438"/><path d="M5.5 4 9 7l-3.5 3" fill="none" stroke="#000" stroke-width="2"/></svg></p>
</div>

<svg class="abs" style="left:0;top:3550px" width="1200" height="145" viewBox="0 0 1200 145">
  <path d="M0 10 C200 90 420 130 640 130 C850 130 1030 90 1200 40 L1200 5 L970 5 C1060 12 1080 18 1060 25 C880 70 700 95 560 95 C350 95 170 60 0 10 Z" fill="var(--red)"/>
</svg>

<div class="abs foot-logo"><span class="brand-mark"></span><p>SILVER HARBOR<br>INSTITUTE</p></div>

<div class="abs" style="left:365px;top:3748px">
  <p class="foot-title">QUICK LINKS</p>
  <div class="foot-links" style="margin-top:12px">Home<br>About Us<br>Services<br>Videos<br>Blog<br>Contact Us</div>
</div>
<div class="abs" style="left:521px;top:3748px;width:270px">
  <p class="foot-title">CONTACT US</p>
  <div style="margin-top:22px">
    <div class="contact-row"><i><svg width="12" height="12" viewBox="0 0 12 12"><path d="M2.5 1h2l1 3-1.5 1a7 7 0 0 0 3 3l1-1.5 3 1v2c0 .6-.5 1-1 1A10 10 0 0 1 1.5 2c0-.5.4-1 1-1z" fill="#f04438"/></svg></i><span style="padding-top:3px">+1 555 204 7781</span></div>
    <div class="contact-row"><i><svg width="12" height="10" viewBox="0 0 12 10"><rect x="0.7" y="0.7" width="10.6" height="8.6" fill="none" stroke="#f04438" stroke-width="1.4"/><path d="M1 1l5 4 5-4" fill="none" stroke="#f04438" stroke-width="1.4"/></svg></i><span style="padding-top:3px">info@silverharborinstitute.com</span></div>
    <div class="contact-row"><i><svg width="10" height="13" viewBox="0 0 10 13"><path d="M5 12.5S.8 7.6.8 4.8a4.2 4.2 0 0 1 8.4 0C9.2 7.6 5 12.5 5 12.5z" fill="#f04438"/><circle cx="5" cy="4.8" r="1.6" fill="#262626"/></svg></i><span>123, Lorem ipsum dolor sit amet, consectetur adipiscing elit sed</span></div>
  </div>
</div>
<div class="abs" style="left:834px;top:3748px;width:254px">
  <p class="foot-title">SUBSCRIBE TO OUR BLOG</p>
  <p style="font-size:11px;line-height:20px;margin-top:18px">Sign up today to get resources on how to attract and retain more customers!</p>
</div>
<div class="abs subscribe">✉ Email Address</div>
<div class="abs subscribe-btn"><svg width="16" height="16" viewBox="0 0 16 16"><path d="M15 1 1 7l5 2 2 5z" fill="#fff"/><path d="M15 1 6 9" stroke="#f04438" stroke-width="1.2"/></svg></div>
<span class="social" style="left:832px" aria-label="Share"><svg width="14" height="14" viewBox="0 0 14 14"><circle cx="3" cy="7" r="2"/><circle cx="11" cy="3" r="2"/><circle cx="11" cy="11" r="2"/><path d="M5 6l4-2M5 8l4 2"/></svg></span>
<span class="social on" style="left:872px" aria-label="Web"><svg width="14" height="14" viewBox="0 0 14 14"><circle cx="7" cy="7" r="6"/><path d="M1 7h12M7 1c2 2 2 10 0 12M7 1c-2 2-2 10 0 12"/></svg></span>
<span class="social" style="left:912px" aria-label="Message"><svg width="14" height="14" viewBox="0 0 14 14"><path d="M1.5 2.5h11v7H6l-3 2.5v-2.5H1.5z"/></svg></span>
<span class="social" style="left:952px" aria-label="Link"><svg width="14" height="14" viewBox="0 0 14 14"><path d="M6 8a3 3 0 0 0 4 0l2-2a2.8 2.8 0 0 0-4-4l-1 1"/><path d="M8 6a3 3 0 0 0-4 0L2 8a2.8 2.8 0 0 0 4 4l1-1"/></svg></span>
<span class="abs chat"><svg width="18" height="16" viewBox="0 0 18 16"><path d="M2 1h14a1 1 0 0 1 1 1v8a1 1 0 0 1-1 1H8l-4 3.5V11H2a1 1 0 0 1-1-1V2a1 1 0 0 1 1-1z" fill="#fff"/><circle cx="5.5" cy="6" r="1" fill="#f04438"/><circle cx="9" cy="6" r="1" fill="#f04438"/><circle cx="12.5" cy="6" r="1" fill="#f04438"/></svg></span>

<div class="abs bottom-bar">
  <span class="abs" style="left:108px">Copyright© 2022 Silver Harbor Institute | All Rights Reserved</span>
  <span class="abs" style="left:842px">Terms and Conditions &nbsp; | &nbsp; Privacy Policy</span>
</div>

</body>
</html>
```